A 24' X 36" SIGN TO ANNOUNCE "ORDER EARLY FOR THE HOLIDAYS

sign is to announce order "early for the holidays"
The design should be festive and leaning towards nostalgic and antique. We are a 100yr old butcher shop. Sign is to list options for customers to include
gkbn prime filet mignon
prime rib roast
goose
duck
pheasant
crown roast of pork/lamb
spiral cut smoked hams
sign should have a black backround
also include or logo
Font styles to use
Serif

```html
<!DOCTYPE html>
<html lang="en">
<head>
<meta charset="utf-8">
<title>Order Early for the Holidays — Hollenbeck Market</title>
<link rel="stylesheet" href="https://fonts.googleapis.com/css2?family=Cinzel:wght@400;700&family=Great+Vibes&family=Oswald:wght@500&family=Sorts+Mill+Goudy&display=swap">
<style>
  :root {
    --festive-red: #e42a26;
    --deep-red: #c41512;
    --night-black: #000000;
    --gold-light: #fff3d6;
    --gold-mid: #e8cf98;
    --gold-deep: #b8935a;
    --star-yellow: #f6e61c;
    --snow-white: #ffffff;
  }
  * { margin: 0; padding: 0; box-sizing: border-box; }
  html, body {
    width: 1200px; height: 800px; overflow: hidden;
    background: var(--night-black);
  }
  .sign {
    position: relative; width: 1200px; height: 800px; overflow: hidden;
    background: var(--night-black);
  }
  .sign__backdrop { position: absolute; inset: 0; }

  .ornaments {
    position: absolute; left: 904px; top: 0; width: 284px; height: 392px;
    background: radial-gradient(ellipse at 50% 40%, rgba(255,255,255,0.55), rgba(255,235,220,0.25) 45%, rgba(228,42,38,0) 72%);
  }

  .headline {
    position: absolute; left: 52px; top: 58px;
    font-family: "Cinzel", "Times New Roman", serif; font-weight: 400;
    font-size: 106px; letter-spacing: 1px; line-height: 1;
    background: linear-gradient(180deg, var(--gold-light) 0%, var(--gold-mid) 55%, var(--gold-deep) 100%);
    -webkit-background-clip: text; background-clip: text; color: transparent;
    text-shadow: none; white-space: nowrap;
  }
  .headline__for {
    position: absolute; left: 144px; top: 164px;
    font-family: "Oswald", "Arial Narrow", sans-serif; font-weight: 500;
    font-size: 58px; line-height: 1; color: var(--night-black);
  }
  .headline__script {
    position: absolute; left: 100px; top: 170px;
    font-family: "Great Vibes", cursive; font-size: 168px; line-height: 1.1;
    white-space: nowrap;
    background: linear-gradient(180deg, var(--gold-light) 0%, var(--gold-mid) 50%, var(--gold-deep) 100%);
    -webkit-background-clip: text; background-clip: text; color: transparent;
    padding-right: 20px;
  }

  .menu {
    position: absolute; list-style: none;
    font-family: "Sorts Mill Goudy", "Goudy Old Style", serif;
    font-size: 37px; color: var(--snow-white); line-height: 48px;
  }
  .menu--left { left: 62px; top: 470px; }
  .menu--right { left: 654px; top: 477px; }
  .menu__item { display: flex; align-items: center; gap: 12px; white-space: nowrap; }
  .menu__star { width: 28px; height: 28px; flex: none; }

  .rule {
    position: absolute; top: 702px; height: 4px; background: var(--star-yellow);
  }
  .rule--left { left: 0; width: 680px; }
  .rule--right { left: 1072px; width: 128px; }

  .brand {
    position: absolute; left: 680px; top: 656px; width: 392px; height: 88px;
    display: flex; align-items: center; justify-content: center;
    font-family: "Cinzel", "Times New Roman", serif; font-weight: 700;
    font-size: 28px; letter-spacing: 2px; color: var(--star-yellow);
  }

  .call-to-action {
    position: absolute; left: 66px; top: 712px;
    font-family: "Sorts Mill Goudy", "Goudy Old Style", serif;
    font-size: 48px; line-height: 60px; color: var(--snow-white); white-space: nowrap;
  }
</style>
</head>
<body>
<main class="sign">
  <svg class="sign__backdrop" width="1200" height="800" viewBox="0 0 1200 800" aria-hidden="true">
    <defs>
      <linearGradient id="red-field" x1="0" y1="0" x2="1" y2="1">
        <stop offset="0" stop-color="#e8322c"/>
        <stop offset="1" stop-color="#d81e1a"/>
      </linearGradient>
      <linearGradient id="edge-glow" x1="0" y1="0" x2="1" y2="0">
        <stop offset="0" stop-color="#ffb070" stop-opacity="0"/>
        <stop offset="0.7" stop-color="#ffd6a0" stop-opacity="0.9"/>
        <stop offset="1" stop-color="#ffb070" stop-opacity="0.2"/>
      </linearGradient>
      <symbol id="star-bullet" viewBox="0 0 28 28">
        <g stroke="#f6e61c" stroke-width="2.4" stroke-linecap="round">
          <line x1="14" y1="2" x2="14" y2="26"/>
          <line x1="3.6" y1="8" x2="24.4" y2="20"/>
          <line x1="3.6" y1="20" x2="24.4" y2="8"/>
          <line x1="6" y1="14" x2="22" y2="14"/>
        </g>
      </symbol>
    </defs>
    <rect width="1200" height="800" fill="#000"/>
    <polygon points="0,0 1200,0 1200,436 0,352" fill="url(#red-field)"/>
    <line x1="500" y1="395" x2="1200" y2="436" stroke="url(#edge-glow)" stroke-width="3"/>
  </svg>

  <div class="ornaments" role="img" aria-label="Hanging white paper snowflakes and ring ornaments on strings"></div>

  <h1 class="headline">ORDER EARLY</h1>
  <p class="headline__for">For</p>
  <p class="headline__script">The Holidays</p>

  <ul class="menu menu--left">
    <li class="menu__item"><svg class="menu__star"><use href="#star-bullet"/></svg>Gkbn prime filet mignon</li>
    <li class="menu__item"><svg class="menu__star"><use href="#star-bullet"/></svg>Prime rib roast</li>
    <li class="menu__item"><svg class="menu__star"><use href="#star-bullet"/></svg>Goose</li>
    <li class="menu__item"><svg class="menu__star"><use href="#star-bullet"/></svg>Duck</li>
  </ul>
  <ul class="menu menu--right">
    <li class="menu__item"><svg class="menu__star"><use href="#star-bullet"/></svg>Pheasant</li>
    <li class="menu__item"><svg class="menu__star"><use href="#star-bullet"/></svg>Crown roast of pork/lamb</li>
    <li class="menu__item"><svg class="menu__star"><use href="#star-bullet"/></svg>Spiral cut smoked hams</li>
  </ul>

  <div class="rule rule--left"></div>
  <div class="rule rule--right"></div>
  <div class="brand">HOLLENBECK MARKET</div>

  <p class="call-to-action">Call Us Now 123456 789</p>
</main>
</body>
</html>
```